Olive oil bottle labels, front and back.

Sophisticated uncluttered distinctive eye catching label
Front label:
Label on front like the uploaded file in design but called “Tallow Brook”, (not Marrowind Bay.)
Need to state that it’s extra virgin, cold pressed olive oil, 100% organic, grown and pressed on the Mornington Peninsula.
500 ml
Back label:
Nutritional information table (see label example in uploaded files) including FFA 0.1% Oleic Acid
Storage: airtight in cool dark place
Made and produced in Australia from 100% Australian ingredients,
Harvest date:
Best by:
Batch:
Grown, harvested and bottled at The Hollow, Pettisby Rd. Carrowmere. 3814
The back label on uploaded files has the info requited except they should have address and don't include those industry and Australian made logos.
The front label is what we want, first to plagiarise without copyright infringement gets the gig, thanks.
Labels front and back need be 5 x 13 cm
Gourmet, up-market
- Love "Adorn Regular Garland"

```html
<!DOCTYPE html>
<html lang="en">
<head>
<meta charset="utf-8">
<title>Tallow Brook Olive Oil Labels</title>
<link rel="stylesheet" href="https://fonts.googleapis.com/css2?family=Cinzel:wght@400;500&family=Cormorant+Garamond:wght@400&family=Oswald:wght@400;500&family=Roboto+Condensed:wght@400;700&display=swap">
<style>
  :root {
    --bg-top: #efefef;
    --bg-bottom: #d2d2d2;
    --label-black: #000000;
    --gold: #b5a25f;
    --gold-dark: #8c7c47;
    --gold-light: #c3b589;
    --white: #ffffff;
    --soft-white: #e8e8e8;
    --rule: #6f6546;
    --leaf: #6f8f3a;
    --olive: #9cb83a;
    --ink: #111111;
  }
  * { margin: 0; padding: 0; box-sizing: border-box; }
  html, body { width: 1075px; height: 1200px; overflow: hidden; }
  body {
    background: linear-gradient(180deg, var(--bg-top), var(--bg-bottom));
    position: relative;
    font-family: "Cinzel", serif;
  }
  .label {
    position: absolute;
    top: 117px;
    width: 300px;
    height: 966px;
    background: var(--label-black);
    overflow: hidden;
    box-shadow: 0 12px 30px rgba(0,0,0,.25);
  }
  .label--front { left: 220px; }
  .label--back { left: 555px; }

  /* Front label */
  .brand-band {
    position: absolute; left: 0; top: 0; width: 86px; height: 100%;
    background: linear-gradient(180deg, var(--gold-dark) 0%, var(--gold-light) 45%, var(--gold) 75%, var(--gold-dark) 100%);
  }
  .stripe-field {
    position: absolute; left: 86px; top: 0; width: 214px; height: 320px;
    background: linear-gradient(180deg, #3a3a3a 0%, #1c1c1c 55%, #000 100%);
  }
  .brand-name {
    position: absolute;
    left: 22px; top: 950px;
    transform: rotate(-90deg);
    transform-origin: 0 0;
    white-space: nowrap;
    font-family: "Cormorant Garamond", serif;
    font-size: 104px;
    line-height: 1;
    color: var(--white);
    letter-spacing: 2px;
  }
  .organic {
    position: absolute; right: 6px; top: 8px;
    font-size: 20px; color: var(--soft-white); letter-spacing: 1px;
  }
  .front-olives {
    position: absolute; left: 78px; top: 72px; width: 222px; height: 330px;
    background: radial-gradient(ellipse at 65% 35%, var(--olive) 0%, var(--leaf) 35%, rgba(60,80,40,.4) 65%, transparent 80%);
  }
  .front-type { position: absolute; right: 28px; text-align: right; }
  .extra-virgin {
    top: 470px; font-size: 31px; line-height: 40px; color: var(--white);
  }
  .rule {
    position: absolute; right: 28px; width: 92px; height: 1px; background: var(--rule);
  }
  .rule--upper { top: 560px; }
  .rule--lower { top: 596px; }
  .coldpressed {
    top: 566px; font-size: 19px; color: var(--gold); letter-spacing: 2px;
  }
  .olive-oil {
    top: 612px; font-size: 54px; line-height: 56px; color: var(--gold);
  }
  .volume {
    top: 886px; right: 17px; font-family: "Oswald", sans-serif; font-weight: 400;
    font-size: 25px; color: var(--gold);
  }
  .origin {
    top: 925px; right: 17px; font-size: 11px; line-height: 16px; color: var(--soft-white); letter-spacing: .5px;
  }
  .origin small { font-size: 9px; }

  /* Back label */
  .back-head { position: absolute; left: 0; width: 100%; text-align: center; }
  .back-extra { top: 42px; font-size: 17px; color: var(--soft-white); letter-spacing: 2px; }
  .back-cold { top: 68px; font-size: 12px; color: var(--soft-white); letter-spacing: 6px; }
  .back-olive { top: 86px; font-size: 31px; color: var(--gold); letter-spacing: 2px; }

  .nutrition {
    position: absolute; left: 24px; top: 145px; width: 254px;
    border: 1px solid #9a9a9a;
    font-family: "Roboto Condensed", sans-serif;
    font-size: 9.5px; color: var(--soft-white);
    padding: 2px 6px 6px;
  }
  .nutrition h3 {
    font-family: "Roboto Condensed", sans-serif; font-weight: 700;
    font-size: 10.5px; letter-spacing: 5px; text-align: center; color: var(--white);
    border-bottom: 1px solid #9a9a9a; margin: 0 -6px 2px; padding-bottom: 2px;
  }
  .nutrition table { width: 100%; border-collapse: collapse; }
  .nutrition td { height: 16.5px; padding: 0; }
  .nutrition td.num { text-align: right; width: 56px; }
  .nutrition tr.units td { height: 32px; vertical-align: top; }

  .back-notes {
    position: absolute; left: 30px; width: 260px;
    font-family: "Roboto Condensed", sans-serif; font-size: 9.5px; color: var(--soft-white);
  }
  .note-ffa { top: 424px; }
  .note-storage { top: 449px; }
  .note-ingredients { top: 474px; }
  .back-notes strong { text-decoration: underline; font-weight: 700; }
  .made-in {
    position: absolute; left: 0; width: 100%; top: 491px; text-align: center;
    font-family: "Roboto Condensed", sans-serif; font-size: 11px; line-height: 19px;
    color: var(--gold); letter-spacing: 1px;
  }
  .back-olives {
    position: absolute; left: 0; top: 540px; width: 298px; height: 185px;
    background: radial-gradient(ellipse at 55% 50%, var(--olive) 0%, var(--leaf) 30%, rgba(60,90,40,.35) 60%, transparent 78%);
  }
  .grown-at {
    position: absolute; left: 30px; top: 730px;
    font-family: "Roboto Condensed", sans-serif; font-size: 12px; line-height: 21px; color: var(--soft-white);
  }
  .batch-panel {
    position: absolute; left: 0; bottom: 0; width: 100%; height: 193px;
    background: var(--white);
    padding: 114px 0 0 15px;
    font-family: "Roboto Condensed", sans-serif; font-size: 13px; line-height: 24px; color: var(--ink);
  }
</style>
</head>
<body>

<section class="label label--front" aria-label="Front label">
  <div class="brand-band"></div>
  <div class="stripe-field" role="img" aria-label="Fine vertical pinstripe pattern fading to black"></div>
  <div class="front-olives" role="img" aria-label="Illustration of a sprig of green olives with leaves"></div>
  <div class="brand-name">Tallow Brook</div>
  <p class="organic">100% Organic</p>
  <p class="front-type extra-virgin">Extra<br>Virgin</p>
  <span class="rule rule--upper"></span>
  <p class="front-type coldpressed">COLDPRESSED</p>
  <span class="rule rule--lower"></span>
  <p class="front-type olive-oil">Olive<br>Oil</p>
  <p class="front-type volume">500 ML</p>
  <p class="front-type origin">Grown and Pressed<br><small>on the Mornington Peninsula</small></p>
</section>

<section class="label label--back" aria-label="Back label">
  <p class="back-head back-extra">Extra Virgin</p>
  <p class="back-head back-cold">COLDPRESSED</p>
  <p class="back-head back-olive">Olive Oil</p>

  <div class="nutrition">
    <h3>NUTRITION INFORMATION</h3>
    <table>
      <tr class="units"><td>AVG&nbsp;&nbsp; QTY</td><td class="num">PER<br>15ml</td><td class="num">PER<br>100ml</td></tr>
      <tr><td>ENERGY (KJ)</td><td class="num">517</td><td class="num">3446</td></tr>
      <tr><td>PROTEIN (G)</td><td class="num">0</td><td class="num">0</td></tr>
      <tr><td>FAT (G)</td><td class="num"></td><td class="num"></td></tr>
      <tr><td>- TOTAL</td><td class="num">13.7</td><td class="num">91.5</td></tr>
      <tr><td>- SATURATED</td><td class="num">2.1</td><td class="num">14.1</td></tr>
      <tr><td>- MONO UNSATURATED</td><td class="num">10.7</td><td class="num">71.5</td></tr>
      <tr><td>- POLY UNSATURATED</td><td class="num">0.9</td><td class="num">5.9</td></tr>
      <tr><td>- TRANS FATTY ACID</td><td class="num">&lt;0.01</td><td class="num">&lt;0.05</td></tr>
      <tr><td>CHOLESTEROL (MG)</td><td class="num">0</td><td class="num">0</td></tr>
      <tr><td>CARBOHYDRATE (G)</td><td class="num">0</td><td class="num">0</td></tr>
      <tr><td>- SUGAR (G)</td><td class="num">0</td><td class="num">0</td></tr>
    </table>
  </div>

  <p class="back-notes note-ffa">FFA 0.1% OLEIC ACID</p>
  <p class="back-notes note-storage"><strong>STORAGE :</strong> STORE AIRTIGHT IN A COOL, DARK PLACE</p>
  <p class="back-notes note-ingredients"><strong>INGREDIENTS :</strong></p>
  <p class="made-in">MADE AND PRODUCED IN AUSTRALIA<br>FROM 100% AUSTRALIAN INGREDIENTS</p>

  <div class="back-olives" role="img" aria-label="Illustration of an olive branch with green olives"></div>

  <p class="grown-at">Grown, Harvested and Bottled at<br>The Hollow, Pettisby Rd. Carrowmere.</p>

  <div class="batch-panel">
    <p>Harvest date:</p>
    <p>Best by:</p>
    <p>Batch:</p>
  </div>
</section>

</body>
</html>
```